Tourism Marketing needing sleek, clear design for business card & proposal documents.

***Company background***
"Quiet Harbour" is a company specializing in tourism marketing and project management. We do international wholesale, event management as well as ongoing representation of tourism and hospitality companies.

***Target market***
We cater to tourism companies and hotel professionals.

***Task***
We would like to get a single sided business card designed (but will still consider two sided, we are open to any ideas you may have). The layout for this card should be modern and elegant. Currently we do not have a logo, but we would like our business name in a really simple typography for the business card (similar to Moonrise Palace's logo - www.moonrisepalace-example.com.au).We are after a design that is clear, strong enough to be recognised as Quiet Harbour that does not require any fancy design. Another option is a simple play on QH (Quiet Harbour) or simply have Quiet Harbour featured elsewhere on card more as a brand/logo.

Feel free to submit different fonts if you feel you have any other fonts/designs that may be suitable for this card other than sans serifs. Should this project be successful, we will be considering several other projects for business proposal templates and eventually a website design.

The information that needs to go on the card are as follows:

Marta Holloway
Director
Quiet Harbour
Tourism Marketing & Representation
87 Wendover Parade
Prahran, Victoria, 3181 Australia
T +61 498203617 E marta@quietharbour-example.com.au

***Look and feel***
We'd like the business card design to express the following:
Modern, sleek, elegant, simple, discreet, quality, subtle, professional, creative, innovation

In terms of typography, we like something really simple and blocky (similar font to Moonrise Palace's logo - www.moonrisepalace-example.com.au)

***Colour scheme***
Shades of grey and dark teal

***Note***
Although our main target market are professionals, we would like the business card design to be versatile enough to be used outside of the tourism industry and need to appeal to different markets.

I do not have existing logo. Was hoping for a design that may be clear, strong enough not to require one. Other option is a simple play on QH (Quiet Harbour) or simply have Quiet Harbour featured elsewhere on card more as a brand/logo.

Marta Holloway
Director
Quiet Harbour Pty Ltd 
87 Wendover Parade
T +61 498203617  E  marta@quietharbour-example.com.au

Thank you for designs so far. Many have used a mauve colour which matches our company profile. This is not necessary, as that is just a draft and will be completely redesigned, so dont  feel you need to incorporate the mauve.

My colour preferences are for a white or grey background, and I like fonts in dark teals, grey or other sophisticated but modern colours. feel free to submit different fonts if you you have other fonts you thing would be suitable for this card, along with sans serifs. Should this project be successful, we will be considering several others for business proposal templates and eventually website. 

Target Market(s)

International Hospitality Senior Executives, Directors of International Tourism Companies, Directors of Tourism Bodies Internationally, local Tourism

Industry/Entity Type

Hospitality

Requirements
Should not have
• must not have bright garish colour, swirly patterns or anything that dates too much.

```html
<!DOCTYPE html>
<html lang="en">
<head>
<meta charset="utf-8">
<title>Quiet Harbour – Business Card</title>
<link rel="stylesheet" href="https://fonts.googleapis.com/css2?family=Roboto:wght@300;400&display=swap">
<style>
  :root {
    --page: #ffffff;
    --card-light: #f8f8fa;
    --card-edge: #ececee;
    --charcoal: #5a5a5c;
    --accent: #b5d334;
    --text-grey: #6e6e70;
    --text-white: #ffffff;
    --text-soft: #b9b9bb;
  }
  * { margin: 0; padding: 0; box-sizing: border-box; }
  html, body {
    width: 1200px; height: 928px; overflow: hidden;
    background: var(--page);
    font-family: "Roboto", Arial, sans-serif;
  }
  .canvas { position: relative; width: 1200px; height: 928px; }

  .card { position: absolute; width: 550px; height: 291px; overflow: hidden; }

  /* Brand name in the card's own text font, one colour, one weight */
  .brand { position: absolute; }
  .brand__name {
    font-family: "Roboto", Arial, sans-serif;
    font-weight: 400; color: var(--accent);
    white-space: nowrap; letter-spacing: 0.5px;
  }
  .brand__tagline {
    font-family: "Roboto", Arial, sans-serif;
    font-weight: 400; text-transform: uppercase; white-space: nowrap;
  }

  /* Front */
  .card--front { left: 129px; top: 175px; background: var(--card-light); border: 1px solid var(--card-edge); }
  .card--front .brand { right: 48px; top: 38px; text-align: right; }
  .card--front .brand__name { font-size: 25px; line-height: 28px; }
  .card--front .brand__tagline { font-size: 8.6px; letter-spacing: 1.2px; color: var(--text-grey); margin-top: 4px; }

  .name-band {
    position: absolute; left: 0; top: 124px; width: 100%; height: 40px;
    background: var(--charcoal);
    display: flex; align-items: center; padding-left: 50px;
  }
  .name-band__name { font-weight: 300; font-size: 17px; color: var(--text-white); }
  .name-band__role { font-weight: 300; font-size: 12.5px; color: var(--accent); margin-left: 34px; margin-top: 2px; }

  .contact { position: absolute; left: 50px; top: 190px; font-weight: 300; color: var(--text-grey); }
  .contact__row { display: flex; align-items: baseline; line-height: 20px; }
  .contact__label { font-size: 7px; color: var(--accent); width: 20px; }
  .contact__phone { font-size: 15px; }
  .contact__email { font-size: 13.5px; }

  .address {
    position: absolute; right: 47px; top: 189px;
    text-align: right; font-style: normal; font-weight: 300;
    font-size: 14.5px; line-height: 20.5px; color: var(--text-grey);
  }

  /* Back */
  .card--back { left: 535px; top: 449px; background: var(--charcoal); }
  .card--back .brand { left: 0; right: 0; top: 100px; text-align: center; }
  .card--back .brand__name { font-size: 34px; line-height: 38px; }
  .card--back .brand__tagline { font-size: 11px; letter-spacing: 1.8px; color: var(--text-white); margin-top: 6px; }
  .web { position: absolute; left: 0; right: 0; top: 235px; text-align: center; font-weight: 300; font-size: 15px; color: var(--text-soft); }
</style>
</head>
<body>
<main class="canvas">
  <section class="card card--front" aria-label="Business card front">
    <div class="brand">
      <div class="brand__name">Quiet Harbour</div>
      <div class="brand__tagline">Hospitality Promotion + Management</div>
    </div>
    <div class="name-band">
      <span class="name-band__name">Marta Holloway</span>
      <span class="name-band__role">director</span>
    </div>
    <div class="contact">
      <div class="contact__row"><span class="contact__label">t</span><span class="contact__phone">+61 498203617</span></div>
      <div class="contact__row"><span class="contact__label">e</span><span class="contact__email">marta@quietharbour-example.com.au</span></div>
    </div>
    <address class="address">
      87 Wendover Parade<br>
      Kestrel Point&nbsp; Victoria<br>
      Australia&nbsp; 3999
    </address>
  </section>

  <section class="card card--back" aria-label="Business card back">
    <div class="brand">
      <div class="brand__name">Quiet Harbour</div>
      <div class="brand__tagline">Hospitality Promotion + Management</div>
    </div>
    <div class="web">quietharbour-example.com.au</div>
  </section>
</main>
</body>
</html>
```